BRVL web site redesign

Coastal Linkwork Systems service (BRVL) is a diverse technology company specialising in design and installation of fibre optics, network convergence and building services, for commercial clients in Australia, we required a new design of our website to attract new clients, generate sales leads, and provide information about our services to the market. The site and should have a new technology look and feel and be designed in word press. our branding colour is blue.

Target Market(s)

New developments, Construction organisations, Commercial end users, IT managers, Consultants.

Industry/Entity Type

It Company

Number of Pages Required

5+ page

Font styles to use
Sans Serif

Colors
0292cd
3176b5

Requirements
Must have
• key pages.
• Home page with some sizzle, automated pictures running through, I like the look of this competitor website http://www.tarelmesh.com.au/ good clean menus and easy to navigate.
• Services page our key services are Fibre optics, Security, Building services,Electrical. I would like the same page layout (Design) for all our services, with a find out more link on each page, manly picture driven with text around our key messaging.
• About us page with space for company profile and directors pictures, bio and contact information.
• Certifications / Accreditations page with have over 20 certifications on different products from suppliers, and a number of licences from governing bodies.
• Current and past projects page with case studies and customer outcomes
• Contact us page with options around what services they require more information on, please keep in mind the site is around generating sales Leeds and being seen as an industry expert.
Nice to have
• RSS feeds, Linked in link, to be placed within the design, Consistent BRVL branding,Same colour blue as our logo Document library for education information, white papers, presentations etc,
• a new technology look and feel, mobile friendly.
Should not have
• boring layout, move away from our cuurent website http://www.brvlgroup.com.au/
• no e eCommerce store required.

```html
<!DOCTYPE html>
<html lang="en">
<head>
<meta charset="utf-8">
<title>BRVL – Coastal Linkwork Systems service</title>
<link href="https://fonts.googleapis.com/css2?family=Roboto:wght@400;500;700&display=swap" rel="stylesheet">
<style>
:root{
  --blue:#3176b5;
  --cyan:#0292cd;
  --ink:#333;
  --muted:#555;
  --light:#efefef;
  --black:#0d0d0d;
  --white:#fff;
  --orange:#f0892a;
}
*{margin:0;padding:0;box-sizing:border-box}
html,body{width:1200px;height:2192px;overflow:hidden}
body{font-family:'Roboto',Arial,sans-serif;color:var(--ink);background:var(--white);position:relative}
.abs{position:absolute}
/* header / hero */
.hero{left:0;top:0;width:1200px;height:636px;background:linear-gradient(135deg,#4a4f55 0%,#2a2d31 40%,#3c6f9a 70%,#5b5e62 100%)}
.navbar{left:0;top:0;width:1200px;height:63px;background:rgba(20,20,20,.55)}
.logo{left:89px;top:0;width:216px;height:110px;background:var(--white);padding:6px}
.logo-inner{width:100%;height:100%;background:var(--blue);display:flex;align-items:center;justify-content:center;gap:12px;color:var(--white);font-weight:700;font-size:40px}
.logo-mark{width:22px;height:22px;background:var(--white)}
.nav a{position:absolute;top:24px;font-size:12.5px;color:var(--white);text-decoration:none;text-transform:uppercase}
.nav a.active{color:var(--cyan)}
.dropdown{left:520px;top:63px;width:149px;height:109px;background:rgba(40,40,40,.8);padding:12px 0 0 16px}
.dropdown li{list-style:none;color:var(--white);font-size:12.5px;line-height:22.5px}
.dropdown li::before{content:"›";margin-right:8px}
.caption{left:115px;top:270px;width:477px;height:180px;background:rgba(50,50,50,.6);padding:34px 28px}
.caption h1{font-size:55px;font-weight:700;color:var(--white);line-height:1}
.caption p{font-size:35px;color:var(--white);margin-top:14px}
.arrow{top:325px}
/* welcome */
.welcome{left:0;top:636px;width:1200px;height:263px;text-align:center}
.welcome h2{position:absolute;top:42px;width:100%;font-size:22px;font-weight:500;color:var(--blue)}
.welcome p{position:absolute;left:105px;top:82px;width:990px;font-size:14px;line-height:26px;color:var(--muted)}
.btn-blue{left:539px;top:184px;width:120px;height:36px;background:var(--cyan);border:2px solid #1a6fa8;border-radius:3px;color:var(--white);font-size:13px;font-weight:500;line-height:32px;text-align:center}
/* services */
.services{left:0;top:899px;width:1200px;height:370px;background:linear-gradient(90deg,#2b88ba,#2f98c8 50%,#2a86b8)}
.services h2{position:absolute;top:26px;width:100%;text-align:center;color:var(--white);font-size:26px;font-weight:500}
.card{top:82px;width:250px}
.card .img{width:250px;height:130px;border:2px solid #e6e6e6}
.card h3{margin-top:15px;font-size:19px;font-weight:500;color:var(--white)}
.card p{margin-top:6px;font-size:12.5px;line-height:18px;color:var(--white);text-align:justify}
.btn-grey{display:block;margin-top:14px;width:94px;height:34px;background:#f2f2f2;border-radius:2px;font-size:13px;line-height:34px;text-align:center;color:var(--ink)}
/* projects */
.projects{left:0;top:1269px;width:1200px;height:419px;background:linear-gradient(135deg,#bdbdbd,#e3e3e3 50%,#b5b5b5)}
.projects h2{position:absolute;top:46px;width:100%;text-align:center;font-size:26px;font-weight:500;color:#222}
.project-card{left:89px;top:109px;width:1028px;height:262px;background:#f7f7f7;border:2px solid #ddd;box-shadow:0 2px 6px rgba(0,0,0,.25)}
.project-img{left:0;top:0;width:402px;height:258px;background:linear-gradient(180deg,#5d8fcf,#9fbbe0 45%,#4d5a4c 100%)}
.project-body{left:423px;top:24px;width:580px}
.project-body h3{font-size:27px;font-weight:400;color:var(--cyan)}
.project-body p{font-size:12.5px;line-height:23.5px;color:#444;margin-top:10px}
.project-body a{color:var(--cyan);text-decoration:none}
.pager{top:18px;width:30px;height:22px;border:1px solid var(--blue);background:var(--white)}
/* call band */
.call{left:0;top:1688px;width:1200px;height:132px;background:var(--blue)}
.call-text{left:189px;top:38px;font-size:41px;color:var(--white)}
.btn-contact{left:801px;top:37px;width:275px;height:57px;background:linear-gradient(#1c9ad8,#1581c0);border:2px solid #5cb7e6;border-radius:3px;color:var(--white);font-size:22px;font-weight:500;line-height:53px;text-align:center}
/* footer info */
.info{left:0;top:1820px;width:1200px;height:219px;background:var(--light)}
.col{top:40px}
.col h4{font-size:17px;font-weight:400;color:var(--blue);margin-bottom:16px}
.col p{font-size:11px;line-height:18px;color:var(--muted)}
.news{display:flex;gap:14px;margin-bottom:14px}
.thumb{width:64px;height:52px;border:2px solid var(--white);box-shadow:0 0 2px #999;flex:none}
.date{color:var(--cyan)}
.rss-box{width:58px;height:58px;background:var(--orange);border-radius:6px;flex:none}
.rss-link{color:var(--orange);text-decoration:underline}
/* bottom */
.bottom{left:0;top:2039px;width:1200px;height:153px;background:var(--black);color:var(--white)}
.bottom .links{left:89px;top:58px;font-size:12px}
.bottom .copy{left:89px;top:82px;font-size:12px}
.social-title{left:798px;top:61px;font-size:12px}
.social-sub{left:798px;top:83px;font-size:10.5px}
.social{top:59px;width:36px;height:36px;border-radius:50%;border:3px solid var(--white)}
</style>
</head>
<body>

<header class="abs hero" role="img" aria-label="Technician working with a fibre optic fusion splicer and green fibre cables"></header>
<div class="abs navbar"></div>
<div class="abs logo"><div class="logo-inner"><span class="logo-mark"></span>BRVL</div></div>
<nav class="nav">
  <a style="left:457px">Home</a>
  <a class="active" style="left:519px">Services ▾</a>
  <a style="left:617px">About us</a>
  <a style="left:706px">Certifications</a>
  <a style="left:840px">Current / Past Projects</a>
  <a style="left:1038px">Contact us</a>
</nav>
<ul class="abs dropdown">
  <li>Fibre optics</li><li>Security</li><li>Building services</li><li>Electrical</li>
</ul>
<div class="abs caption"><h1>FIBRE OPTICS</h1><p>Installation and solutions</p></div>
<svg class="abs arrow" style="left:56px" width="34" height="66" viewBox="0 0 34 66"><path d="M30 2 L4 33 L30 64" fill="none" stroke="#fff" stroke-width="2"/></svg>
<svg class="abs arrow" style="left:1110px" width="34" height="66" viewBox="0 0 34 66"><path d="M4 2 L30 33 L4 64" fill="none" stroke="#fff" stroke-width="2"/></svg>

<section class="abs welcome">
  <h2>WELCOME TO BRVL GROUP</h2>
  <p>Lorem Ipsum has been the industry's standard dummy text ever since the 1500s, when an unknown printer took a galley of type and scrambled it to make a type specimen book. It has survived not only five centuries, but also the leap into electronic typesetting, remaining essentially unchanged. It was popularised in the 1960s with the release of Lettrex sheets containing Lorem Ipsum passages, and more recently with desktop publishing software</p>
  <div class="abs btn-blue">READ MORE</div>
</section>

<section class="abs services">
  <h2>SERVICES</h2>
  <div class="abs card" style="left:89px">
    <div class="img" role="img" aria-label="Glowing blue fibre optic strands" style="background:radial-gradient(circle at 70% 70%,#3fc3e8,#0a3a5a 60%,#01121e)"></div>
    <h3>FIBRE OPTICS</h3>
    <p>Duis aute irure dolor in reprehenderit in voluptate velit esse cillum dolore eu fugiat</p>
    <span class="btn-grey">Read More</span>
  </div>
  <div class="abs card" style="left:348px">
    <div class="img" role="img" aria-label="Technician with a laptop beside a network cabinet" style="background:linear-gradient(90deg,#8a8f94,#d9dadc 55%,#f2f2f2)"></div>
    <h3>SECURITY</h3>
    <p>Duis aute irure dolor in reprehenderit in voluptate velit esse cillum dolore eu fugiat</p>
    <span class="btn-grey">Read More</span>
  </div>
  <div class="abs card" style="left:607px">
    <div class="img" role="img" aria-label="Engineers in hard hats on a construction site" style="background:linear-gradient(180deg,#c9ccd0,#8d7a5e 60%,#5d4a35)"></div>
    <h3>BUILDING SERVICES</h3>
    <p>Duis aute irure dolor in reprehenderit in voluptate velit esse cillum dolore eu fugiat</p>
    <span class="btn-grey">Read More</span>
  </div>
  <div class="abs card" style="left:866px">
    <div class="img" role="img" aria-label="Row of orange electrical switchboards" style="background:linear-gradient(90deg,#c8561c,#e8792c 50%,#b9a18a)"></div>
    <h3>ELECTRICAL</h3>
    <p>Duis aute irure dolor in reprehenderit in voluptate velit esse cillum dolore eu fugiat</p>
    <span class="btn-grey">Read More</span>
  </div>
</section>

<section class="abs projects">
  <h2>RECENT PROJECTS</h2>
  <div class="abs project-card">
    <div class="abs project-img" role="img" aria-label="Tall residential tower covered in vertical gardens against a blue sky"></div>
    <div class="abs project-body">
      <h3>Harbourline Tower</h3>
      <p>Marrow Bay Central occupies nearly six hectares of the southern Marrow Bay CBD, defining Marrow Bay's ‘downtown’. Marrow Central is the kestrel-1 visionary redevelopment of the old Halden &amp; Pike Mill site, bordered by Tallow and Fenwick Streets in Wrenfield.<br><br>The site includes the protection of heritage buildings, new parklands and community facilities and substantial upgrades to urban infrastructure. <a>Read More &gt;&gt;</a></p>
    </div>
    <svg class="abs pager" style="left:944px" viewBox="0 0 30 22"><path d="M18 6 L12 11 L18 16" fill="none" stroke="#3176b5" stroke-width="1.6"/></svg>
    <svg class="abs pager" style="left:980px" viewBox="0 0 30 22"><path d="M12 6 L18 11 L12 16" fill="none" stroke="#3176b5" stroke-width="1.6"/></svg>
  </div>
</section>

<section class="abs call">
  <svg class="abs" style="left:106px;top:37px" width="60" height="60" viewBox="0 0 60 60">
    <circle cx="30" cy="30" r="27" fill="none" stroke="#fff" stroke-width="3"/>
    <path d="M22 17c2-1 4 0 5 2l2 5c0 2-1 3-2 4 1 3 4 6 7 7 1-1 2-2 4-2l5 2c2 1 3 3 2 5-1 3-4 4-7 3-9-2-16-9-18-18-1-3 0-6 2-8z" fill="#fff"/>
  </svg>
  <div class="abs call-text">Call Us Today ! 1300 555 014</div>
  <div class="abs btn-contact">CONTACT US</div>
</section>

<section class="abs info">
  <div class="abs col" style="left:89px;width:250px">
    <h4>CONTACT INFO</h4>
    <p>Suite 4B, 12-14 Corran Avenue<br>Elmstone NSW 2150<br>PO Box 2048 NSW 1760</p>
    <p style="margin-top:12px">
      <svg width="10" height="10" viewBox="0 0 10 10" style="margin-right:10px"><path d="M2 1l2 2-1 1.5c.6 1.2 1.3 1.9 2.5 2.5L7 6l2 2-1.5 1.5C5 9 1 5 .5 2.5z" fill="#3176b5"/></svg>1300 555 014<br>
      <svg width="10" height="8" viewBox="0 0 10 8" style="margin-right:10px"><rect width="10" height="8" fill="#3176b5"/><path d="M0 0l5 4 5-4" fill="none" stroke="#fff"/></svg>info@brvlmail.example
    </p>
  </div>
  <div class="abs col" style="left:398px;width:330px">
    <h4>LATEST NEWS</h4>
    <div class="news"><div class="thumb" role="img" aria-label="Aerial view of a green building site" style="background:linear-gradient(135deg,#3c6a3c,#a8b8a0)"></div><p>Lorem ipsum dolor sit amet, consectetur adipisicing elit, sed do eiusmod tempor<br><span class="date">july 7, 2015</span></p></div>
    <div class="news"><div class="thumb" role="img" aria-label="City street with buildings" style="background:linear-gradient(135deg,#9fbbe0,#c98a6a)"></div><p>Lorem ipsum dolor sit amet, consectetur adipisicing elit, sed do eiusmod tempor<br><span class="date">july 7, 2015</span></p></div>
  </div>
  <div class="abs col" style="left:842px;width:275px">
    <h4>RSS FEED</h4>
    <p>Lorem ipsum dolor sit amet, consectetur adipisicing elit, sed do eiusmod tempor</p>
    <div class="news" style="margin-top:16px"><div class="rss-box"></div><p>Lorem ipsum dolor sit amet, consectetur adipisicing elit, sed do eiusmod tempor<br><span class="rss-link">Links</span></p></div>
  </div>
</section>

<footer class="abs bottom">
  <div class="abs links">HOME &nbsp;|&nbsp; ABOUT &nbsp;|&nbsp; NEWS &nbsp;|&nbsp; BLOG &nbsp;|&nbsp; CONTACTS</div>
  <div class="abs copy">© 2015 &nbsp;Privacy Policy</div>
  <div class="abs social-title">SOCIAL NETWORKS</div>
  <div class="abs social-sub">Lorem Ipsum is simply dummy text</div>
  <div class="abs social" style="left:994px;background:#2a8fd0"></div>
  <div class="abs social" style="left:1037px;background:#d52b1e"></div>
  <div class="abs social" style="left:1079px;background:#f0652a"></div>
</footer>

</body>
</html>
```